3 x 3 metre trade booth design

We need a design for a 3 x 3 metre corner booth for a conference we are attending. There will therefore be 2 x backdrops that we need to have designed. For one of them we want to have our services displayed as an engaging, modern infographic. For the other, we would like to have our brand tagline and our logo, with a cool background which aligns with what we do.
I have attached a picture of what our booth looked like last year- we designed this ourself and we need it to look much more professional, with a different type of infographic for the
Please see attachment with full design brief attached

```html
<!DOCTYPE html>
<html lang="en">
<head>
<meta charset="utf-8">
<title>Quantella Corner Booth Backdrops</title>
<link href="https://fonts.googleapis.com/css2?family=Montserrat:wght@400;500;600;700;800&display=swap" rel="stylesheet">
<style>
  :root {
    --stage: #8c8c8c;
    --white: #ffffff;
    --ink: #14121a;
    --purple: #7b3fa6;
    --purple-soft: #8f55b5;
    --gold: #d8a85c;
    --yellow: #f4c72a;
    --night: #181320;
    --plum: #3e2b4b;
    --body-font: "Montserrat", sans-serif;
  }
  * { margin: 0; padding: 0; box-sizing: border-box; }
  html, body { width: 889px; height: 1200px; overflow: hidden; }
  body { background: var(--stage); font-family: var(--body-font); position: relative; }

  .backdrop {
    position: absolute; left: 159px; width: 570px; height: 570px;
    overflow: hidden; box-shadow: 0 10px 22px rgba(0,0,0,.35);
  }
  .backdrop--brand { top: 20px; }
  .backdrop--services { top: 610px; }
  .backdrop__shapes { position: absolute; inset: 0; }

  /* brand panel */
  .brand-mark {
    position: absolute; left: 95px; top: 28px; width: 76px; height: 76px;
    border: 5px solid var(--purple-soft);
  }
  .brand-name {
    position: absolute; left: 196px; top: 46px;
    font-weight: 800; font-size: 38px; letter-spacing: 4px; color: var(--ink);
  }
  .brand-tagline {
    position: absolute; left: 200px; top: 94px;
    font-weight: 700; font-size: 10.5px; letter-spacing: 3.4px; color: var(--ink);
  }
  .hero-headline {
    position: absolute; left: 40px; top: 172px; width: 490px;
    text-align: center; color: var(--white); transform: rotate(-1.5deg);
  }
  .hero-headline__lead { display: block; font-weight: 500; font-size: 19.5px; letter-spacing: .5px; }
  .hero-headline__main { display: block; font-weight: 800; font-size: 37px; line-height: 1.05; margin-top: 4px; }

  /* services panel */
  .brand-mark--small { left: 38px; top: 44px; width: 36px; height: 36px; border-width: 3px; }
  .brand-name--small { left: 86px; top: 49px; font-size: 17px; letter-spacing: 2px; }
  .brand-tagline--small { left: 87px; top: 71px; font-size: 5px; letter-spacing: 1.4px; }
  .panel-title {
    position: absolute; right: 50px; top: 40px; text-align: right;
    font-weight: 800; font-size: 33px; line-height: 1.05;
  }
  .panel-title__top { display: block; color: var(--ink); }
  .panel-title__bottom { display: block; color: var(--purple); }

  .service { position: absolute; color: var(--white); width: 170px; }
  .service__title { font-weight: 700; font-size: 9.6px; color: var(--yellow); margin-bottom: 3px; white-space: nowrap; }
  .service__list { list-style: none; font-size: 8.1px; line-height: 1.6; font-weight: 400; }
  .service__list li { position: relative; padding-left: 9px; }
  .service__list li::before { content: "•"; position: absolute; left: 0; }

  .service--advertising { left: 130px; top: 219px; }
  .service--content { left: 315px; top: 191px; width: 160px; }
  .service--setup { left: 44px; top: 446px; width: 130px; }
  .service--expansion { left: 222px; top: 446px; width: 130px; }
  .service--management { left: 410px; top: 446px; width: 130px; }
</style>
</head>
<body>

<section class="backdrop backdrop--brand" aria-label="Brand backdrop">
  <svg class="backdrop__shapes" viewBox="0 0 570 570" aria-hidden="true">
    <defs>
      <radialGradient id="photoGlow" cx="0.45" cy="0.8" r="0.75">
        <stop offset="0" stop-color="#3a7fd6"/>
        <stop offset="0.4" stop-color="#143a78"/>
        <stop offset="1" stop-color="#050a1c"/>
      </radialGradient>
      <linearGradient id="bannerFill" x1="0" y1="0" x2="1" y2="0.6">
        <stop offset="0" stop-color="#8a4db3"/>
        <stop offset="0.55" stop-color="#a97095"/>
        <stop offset="1" stop-color="#dcae63"/>
      </linearGradient>
    </defs>
    <rect width="570" height="570" fill="url(#photoGlow)" role="img" aria-label="Photo: glowing rising arrows over a stock market chart and a digital world map"/>
    <polygon points="0,0 570,0 570,132 0,158" fill="var(--white)"/>
    <polygon points="36,157 536,134 526,332 44,305" fill="url(#bannerFill)"/>
  </svg>
  <div class="brand-mark"></div>
  <div class="brand-name">QUANTELLA</div>
  <div class="brand-tagline">ORBIMART MASTERY AGENCY</div>
  <h1 class="hero-headline">
    <span class="hero-headline__lead">TRANSFORMING BRANDS INTO</span>
    <span class="hero-headline__main">ORBIMART SUCCESS<br>STORIES</span>
  </h1>
</section>

<section class="backdrop backdrop--services" aria-label="Services backdrop">
  <svg class="backdrop__shapes" viewBox="0 0 570 570" aria-hidden="true">
    <defs>
      <linearGradient id="nightFill" x1="0" y1="0" x2="0.3" y2="1">
        <stop offset="0" stop-color="#15111a"/>
        <stop offset="0.5" stop-color="#2a1f33"/>
        <stop offset="1" stop-color="#4a3458"/>
      </linearGradient>
      <linearGradient id="iconFill" x1="0" y1="0" x2="0.6" y2="1">
        <stop offset="0" stop-color="#8a4db3"/>
        <stop offset="1" stop-color="#dca963"/>
      </linearGradient>
      <linearGradient id="waveFill" x1="0" y1="0" x2="1" y2="0">
        <stop offset="0" stop-color="#c9a45a" stop-opacity=".35"/>
        <stop offset="1" stop-color="#c9a45a" stop-opacity="0"/>
      </linearGradient>
    </defs>
    <rect width="570" height="570" fill="url(#nightFill)"/>
    <rect x="0" y="140" width="190" height="110" fill="url(#waveFill)" opacity=".5" role="img" aria-label="Decorative gold mesh wave"/>
    <polygon points="0,0 570,0 570,160 0,131" fill="var(--white)"/>

    <g fill="#ffffff" fill-opacity=".06">
      <circle cx="102" cy="357" r="62"/>
      <circle cx="192" cy="357" r="62"/>
      <circle cx="285" cy="357" r="62"/>
      <circle cx="376" cy="357" r="62"/>
      <circle cx="468" cy="357" r="62"/>
    </g>

    <g stroke="#ffffff" stroke-width="1.2" stroke-dasharray="2 3" fill="none">
      <line x1="192" y1="276" x2="192" y2="314"/>
      <line x1="376" y1="276" x2="376" y2="314"/>
      <line x1="102" y1="400" x2="102" y2="436"/>
      <line x1="285" y1="400" x2="285" y2="436"/>
      <line x1="468" y1="400" x2="468" y2="436"/>
    </g>
    <g fill="#ffffff">
      <circle cx="192" cy="276" r="2"/><circle cx="376" cy="276" r="2"/>
      <circle cx="102" cy="436" r="2"/><circle cx="285" cy="436" r="2"/><circle cx="468" cy="436" r="2"/>
    </g>

    <g fill="url(#iconFill)" stroke="#ffffff" stroke-width="5">
      <circle cx="102" cy="357" r="39"/>
      <circle cx="192" cy="357" r="39"/>
      <circle cx="285" cy="357" r="39"/>
      <circle cx="376" cy="357" r="39"/>
      <circle cx="468" cy="357" r="39"/>
    </g>

    <g fill="none" stroke="#fff" stroke-width="2.2" stroke-linejoin="round">
      <rect x="86" y="350" width="32" height="20" rx="2"/>
      <line x1="102" y1="370" x2="102" y2="376"/><line x1="94" y1="377" x2="110" y2="377"/>
      <circle cx="102" cy="347" r="6"/>
    </g>
    <circle cx="102" cy="347" r="2.2" fill="#fff"/>

    <g fill="#fff">
      <polygon points="178,352 198,342 198,372 178,362"/>
      <rect x="172" y="352" width="7" height="10" rx="1"/>
      <rect x="180" y="362" width="5" height="10" rx="1"/>
    </g>
    <g stroke="#fff" stroke-width="2" stroke-linecap="round">
      <line x1="203" y1="357" x2="210" y2="357"/><line x1="202" y1="348" x2="208" y2="344"/><line x1="202" y1="366" x2="208" y2="370"/>
    </g>

    <g fill="none" stroke="#fff" stroke-width="2">
      <circle cx="285" cy="357" r="11"/>
      <ellipse cx="285" cy="357" rx="5" ry="11"/>
      <line x1="274" y1="357" x2="296" y2="357"/>
      <line x1="285" y1="341" x2="285" y2="335"/><line x1="285" y1="373" x2="285" y2="379"/>
      <line x1="269" y1="357" x2="263" y2="357"/><line x1="301" y1="357" x2="307" y2="357"/>
    </g>

    <g fill="none" stroke="#fff" stroke-width="2" stroke-linecap="round">
      <path d="M362 372 q14 6 28 -2"/>
      <line x1="376" y1="366" x2="376" y2="352"/>
      <line x1="376" y1="358" x2="368" y2="350"/><line x1="376" y1="358" x2="384" y2="350"/>
    </g>
    <g fill="#fff"><circle cx="376" cy="347" r="5"/><circle cx="366" cy="348" r="4"/><circle cx="386" cy="348" r="4"/></g>

    <g fill="#fff">
      <circle cx="462" cy="346" r="7"/>
      <path d="M449 372 q0 -15 13 -15 q10 0 12 8 v7 z"/>
    </g>
    <g fill="none" stroke="#fff" stroke-width="2.2"><circle cx="479" cy="366" r="6"/></g>
    <circle cx="479" cy="366" r="2" fill="#fff"/>
  </svg>

  <div class="brand-mark brand-mark--small"></div>
  <div class="brand-name brand-name--small">QUANTELLA</div>
  <div class="brand-tagline brand-tagline--small">ORBIMART MASTERY AGENCY</div>
  <h2 class="panel-title">
    <span class="panel-title__top">FULL SERVICE</span>
    <span class="panel-title__bottom">MANAGEMENT</span>
  </h2>

  <div class="service service--advertising">
    <h3 class="service__title">Orbimart Advertising</h3>
    <ul class="service__list"><li>Paid Search Ads (PPC)</li><li>Bid automation</li><li>Demand-Side Platform (DSP)</li></ul>
  </div>
  <div class="service service--content">
    <h3 class="service__title">Brand Content &amp; Optimisation</h3>
    <ul class="service__list"><li>Rich Content / Premium Brand Content</li><li>Brand store</li><li>Product listing optimisation</li><li>Search Engine Optimisation (SEO)</li></ul>
  </div>
  <div class="service service--setup">
    <h3 class="service__title">Orbimart Account Setup</h3>
    <ul class="service__list"><li>Cost analysis to scale profitably</li><li>Orbimart account setup</li><li>Account audit</li><li>Orbimart Brand Protection</li></ul>
  </div>
  <div class="service service--expansion">
    <h3 class="service__title">International Expansion</h3>
    <ul class="service__list"><li>Market opportunity analysis</li><li>Launch in new marketplaces</li><li>Listing localisation</li><li>Logistics &amp; Fulfilment strategy</li></ul>
  </div>
  <div class="service service--management">
    <h3 class="service__title">Account Management</h3>
    <ul class="service__list"><li>Catalogue management</li><li>Account health monitoring</li><li>Case log &amp; issue resolution</li><li>Fulfilment Inventory Management</li><li>Customised Reporting</li></ul>
  </div>
</section>

</body>
</html>
```